WORDPRESS DESIGN - PROFESSIONAL SERVICES

Objective:
Design a new Wordpress e-commerce website for www.brolvanecareers.com.au .

BRLV Careers provides professional CV/resume writing services for Australian IT professionals. This assignment is to upgrade an existing 25 page e-commerce website - www.brolvanecareers.com.au

Process:
The contract is to design of the website. PixelForum designers need to submit a home page design based on the attached files and wireframes. BRLV will judge these submissions and the winner will be awarded $350 to design the 25 page website for Wordpress

Design:
You will be given Quartzly Wireframes, images and copy to base your design on. You can choose any font or colour palette, although it is preferred if you base it on the existing logo.

The design must be:
• Corporate
• Compelling
• Trustworthy

Development:
Development will be a separate assignment. The existing website to be upgraded is built on WordPress and Tradeloom.

You will be provided:
a) Logo
b) Suggested Colour palette
c) 25 Quartzly Wireframes
d) Images
e) Copy

Process:
1) Submit home page designs based on Home ATF and Home BTF.
2) Winner gets $350 design contract
3) Design sign-off
4) Payment

Target Market(s)

Customer Profile:

• Professional
• IT Professionals
• Earn $100k+
• Corporate
• University/Tertiary Educatation
• 80% men
• Live in Australian cities
• Mix of European, Indian and Asian backgrounds
• 75% are 30-50 y/o

Industry/Entity Type

E-Commerce

Font styles to use
Sans Serif

Colors
0355a3
3176b5
85abd2

Requirements
Must have
• The design must be:
• Corporate
• Compelling
• Trustworthy

* Lay-out should be based on the wireframes provided by BRLV
* The top banner is very important and will be on every page.
* There are a lot of words on the page so one of the challenges is to make it not look crowded and busy.
* It needs to look modern and professional. Use some creativity.
* The three key buttons we want users to click is the 'Click Me' next to products and the 'Shop' icon. Please highlight these (maybe in a different colour or with a frame)
* The font is very important.
Nice to have
• The font and colour palette you choose matches the existing logo

```html
<!DOCTYPE html>
<html lang="en">
<head>
<meta charset="utf-8">
<title>BRLV Careers – CV Writing for IT Professionals</title>
<link href="https://fonts.googleapis.com/css2?family=Arimo:ital,wght@0,400;0,700;1,700&display=swap" rel="stylesheet">
<style>
:root{
  --navy:#0a3f7a;
  --brand:#0355a3;
  --mid:#3176b5;
  --soft:#85abd2;
  --pale:#e6eff8;
  --white:#ffffff;
  --ink:#1a1a1a;
}
*{box-sizing:border-box;margin:0;padding:0}
html,body{width:826px;height:1200px;overflow:hidden;background:var(--white)}
body{font-family:"Arimo",Arial,sans-serif;color:var(--ink);position:relative}
.abs{position:absolute}

/* header */
.header{left:0;top:0;width:826px;height:116px;background:linear-gradient(180deg,#ffffff 0%,#eef4fa 100%)}
.header-art{left:470px;top:0;width:356px;height:116px;background:linear-gradient(100deg,rgba(255,255,255,0) 0%,#c6d8eb 45%,#85abd2 100%)}
.brand{left:20px;top:22px;display:flex;align-items:center;gap:8px}
.brand-dot{width:30px;height:30px;border-radius:50%;background:var(--brand)}
.brand-name{font-size:16px;font-weight:700;color:var(--brand)}
.site-title{left:238px;top:28px;font-size:34px;font-weight:700;font-style:italic;color:var(--navy);letter-spacing:-.3px}

/* nav */
.nav{left:14px;top:118px;width:798px;height:32px;background:linear-gradient(180deg,var(--mid),var(--brand));display:flex;align-items:center}
.nav a{color:var(--white);text-decoration:none;font-size:20px;padding:0 19px;border-right:1px solid var(--soft);line-height:24px}
.nav a.shop{background:var(--white);color:var(--brand);font-weight:700;border-radius:3px;margin:0 6px;padding:0 14px}
.nav .social{margin-left:auto;margin-right:10px;font-size:13px;font-weight:700;color:var(--white);display:flex;align-items:center;gap:6px}
.nav .social i{width:12px;height:12px;background:var(--soft);display:block}
.cart{left:722px;top:153px;font-size:14px;color:var(--navy);display:flex;gap:6px;align-items:center}

/* hero */
.hero{left:14px;top:182px;width:454px;height:268px;background:linear-gradient(180deg,var(--navy),var(--brand) 60%,var(--navy));color:var(--white);padding:10px 14px}
.hero-intro{font-size:10px;line-height:13px;text-align:center;color:var(--pale);width:300px;margin-left:40px}
.hero-h{font-size:26px;line-height:30px}
.hero-sub{font-size:18px;line-height:22px}
.hero-band{left:0;top:190px;width:454px;height:66px;background:rgba(133,171,210,.18)}
.hero-seal{left:352px;top:24px;width:76px;height:76px;border-radius:50%;background:var(--mid)}

/* credentials */
.creds{left:480px;top:187px;width:332px;text-align:right;color:var(--brand)}
.creds h2{font-size:16px;font-weight:700}
.creds ul{list-style:none;font-size:14px;line-height:17px;color:var(--navy)}
.badges{left:490px;top:322px;display:flex;gap:26px;align-items:center}
.contact{left:480px;top:394px;width:332px;height:38px;border:2px solid var(--mid);color:var(--brand);font-size:14px;display:flex;align-items:center;justify-content:center}

/* products */
.product{top:470px;width:220px;height:322px;background:var(--brand);color:var(--white);display:flex;flex-direction:column}
.product-head{padding:8px 10px 6px;font-size:15px;line-height:18px;text-align:center;height:64px}
.rating{background:var(--white);color:var(--navy);margin:0 8px;padding:5px 8px;font-size:11px;display:flex;gap:6px;align-items:center;height:42px}
.rating small{display:block;font-size:9px;color:var(--mid)}
.features{list-style:none;padding:10px 10px;font-size:14px;line-height:24px;flex:1}
.buy{display:flex;height:60px;background:var(--navy)}
.buy-btn{width:108px;margin:8px;background:var(--white);color:var(--ink);font-weight:700;font-size:19px;display:flex;align-items:center;justify-content:center;border:3px solid var(--soft)}
.price{font-size:13px;line-height:18px;padding-top:12px}

/* testimonials */
.testimonials{left:480px;top:456px;width:332px;height:540px;background:linear-gradient(180deg,var(--mid),var(--brand));color:var(--white);display:flex;flex-direction:column;align-items:center;justify-content:center;font-size:30px;line-height:40px}

/* photo */
.photo{left:14px;top:804px;width:454px;height:192px;background:linear-gradient(90deg,#eef3f9 0%,#b9cfe6 50%,#4f82b9 100%)}

/* process */
.process{left:14px;top:1008px;width:456px;font-size:12px;line-height:17px;color:var(--navy)}
.process ol{list-style:none}
.register{left:480px;top:1008px;width:332px;height:76px;border:2px solid var(--soft);background:var(--pale);color:var(--brand);font-size:16px;line-height:20px;text-align:center;display:flex;align-items:center;justify-content:center;padding:0 16px}
</style>
</head>
<body>

<header class="header abs">
  <div class="header-art abs" role="img" aria-label="Decorative blue swoosh banner"></div>
  <div class="brand abs"><span class="brand-dot"></span><span class="brand-name">BRLV Careers</span></div>
  <div class="site-title abs">CV Writing for IT Professionals</div>
</header>

<nav class="nav abs">
  <a href="#">Home</a>
  <a href="#" class="shop">Shop</a>
  <a href="#">Map</a>
  <a href="#">Testimonials</a>
  <a href="#">About us</a>
  <a href="#">Contact us</a>
  <span class="social"><i></i>ProLink</span>
</nav>
<div class="cart abs">
  <svg width="16" height="14" viewBox="0 0 16 14" aria-hidden="true"><path d="M0 1h3l2 8h8l2-6H4" fill="none" stroke="#0a3f7a" stroke-width="1.5"/><circle cx="6" cy="12" r="1.3" fill="#0a3f7a"/><circle cx="12" cy="12" r="1.3" fill="#0a3f7a"/></svg>
  My cart
</div>

<section class="hero abs">
  <div class="hero-band abs"></div>
  <div class="hero-seal abs" role="img" aria-label="Quality seal badge"></div>
  <p class="hero-intro">we deliver IT specialist CV's and ProLink profiles that showcases your value and achieve high search ranking in ProLink and recruitment databases.</p>
  <div style="margin-top:12px">
    <div class="hero-h">Project Services:</div>
    <div class="hero-sub">Architects &nbsp;developers &nbsp;infrastructure</div>
  </div>
  <div style="margin-top:56px">
    <div class="hero-h">Specialist Expertise in:</div>
    <div class="hero-sub" style="margin-top:6px">Executive &nbsp;Management &nbsp;Sales &nbsp;Digital &nbsp;Developers</div>
  </div>
</section>

<section class="creds abs">
  <h2>IT Specialist CV's &amp; ProLink Profiles</h2>
  <ul>
    <li>Proven track record</li>
    <li>200 IT Placements</li>
    <li>100%client Satisfaction</li>
    <li>20,000 IT CV'S Reviewed</li>
    <li>7 Years in IT Recruitment</li>
  </ul>
</section>
<div class="badges abs" role="img" aria-label="Partner and certification badges">
  <svg width="100" height="56" aria-hidden="true"><rect x="0" y="8" width="40" height="40" rx="4" fill="#0355a3"/></svg>
  <svg width="90" height="56" aria-hidden="true"><circle cx="28" cy="28" r="26" fill="#3176b5"/></svg>
  <svg width="56" height="56" aria-hidden="true"><rect x="4" y="4" width="48" height="48" rx="4" fill="#0355a3"/></svg>
</div>
<div class="contact abs">Contact Marcus anytime on +61 3 9555 0142</div>

<svg width="0" height="0" class="abs" aria-hidden="true"><defs><path id="st" d="M6 0l1.8 4 4.2.4-3.2 2.8 1 4.1L6 9.2 2.2 11.3l1-4.1L0 4.4 4.2 4z"/></defs></svg>

<article class="product abs" style="left:14px">
  <div class="product-head">A new CV, cover letter &amp; ProLink profile</div>
  <div class="rating">
    <svg width="58" height="12" aria-hidden="true"><g fill="#0355a3"><use href="#st"/><use href="#st" x="11.5"/><use href="#st" x="23"/><use href="#st" x="34.5"/><use href="#st" x="46"/></g></svg>
    <div>Stars customer rating<small>Testimonials</small></div>
  </div>
  <ul class="features">
    <li>One week</li>
    <li>Dedicated CV writer</li>
    <li>New CV in Wordly</li>
    <li>Optimised ProLink profile</li>
    <li>Money-back guarantee</li>
  </ul>
  <div class="buy"><a class="buy-btn">BUY NOW</a><div class="price">Worth $ 700<br>Only $ 385</div></div>
</article>

<article class="product abs" style="left:248px">
  <div class="product-head">Urgently need a new CV, Cover Letter &amp; ProLink profile in $48 hours</div>
  <div class="rating">
    <svg width="58" height="12" aria-hidden="true"><g fill="#0355a3"><use href="#st"/><use href="#st" x="11.5"/><use href="#st" x="23"/><use href="#st" x="34.5"/><use href="#st" x="46"/></g></svg>
    <div>Stars customer rating<small>Testimonials</small></div>
  </div>
  <ul class="features">
    <li>2 Business day turnaround</li>
    <li>Dedicate CV writer</li>
    <li>New CV in Wordly</li>
    <li>OPtimised ProLink profile</li>
    <li>Money-back guarantee</li>
  </ul>
  <div class="buy"><a class="buy-btn">BUY NOW</a><div class="price">Worth $ 800<br>Only $ 495</div></div>
</article>

<aside class="testimonials abs">
  <span>t</span><span>e</span><span>s</span><span>t</span><span>i</span><span>m</span><span>o</span><span>n</span><span>i</span><span>a</span><span>s</span>
</aside>

<div class="photo abs" role="img" aria-label="Photo of a curriculum vitae page beside a businessman leaping forward with a briefcase"></div>

<section class="process abs">
  <p>HOW WE WILL WRITE YOUR CV AND PROLINK PROFILE:</p>
  <ol>
    <li>1- We start with your career aspirations and most recent CV.</li>
    <li>2- We ask questions by e-mail to fill in any missing information.</li>
    <li>3- We produce 3-4 drafts before delivering the final version.</li>
    <li>4- When you are happy with the result, you approve the CV.</li>
    <li>5- You get a search optimised ProLink profile based &nbsp;on your new CV.</li>
    <li>6- We work however fast or slow you want us to.</li>
  </ol>
</section>

<div class="register abs">Register easily for our free recruitment coaching newsletters and special offers</div>

</body>
</html>
```